Vexo QR

Create flyers for product information
https://vexo-qr.examplestore.test/
Our products are 100% plant extracts
2 patients.
Our base product starts with human homeopathy formula and with the same team of doctors, created vexo-QR.
It’s produced in a laboratory that is certified human grade.
Our standard meets and exceeds all EU and USA requirements
Trials include a university in Germany.
On farms trials, in Asia, Europe, USA,
Australia and Canada.
No milk and meat withdrawals.
It’s produced in The Netherlands. And we meet U.S. and European standards.
3 different types of vexo-QR (for flyer design each):
Package 1
10 doses ready to use ( RTU )
25 mL. Per dose 10 Pipettes 1 bottle of 250 mL vexo-QR. 1 35 ML syringe.
Package 2
33 doses concentrated Vexo-QR.
250 ML bottle of concentrated vexo QR.
33 Pipettes, 1 35 ML syringe.
Mix the full amount of the 250 ML bottle along with 750 mL of sterile saline Solution. Making 1000mL
A 30 ML dose per cow.
Package 3
HORSE
Single dose package of a 40 ML dose RTU.
1 Pipette, 1 40, ML bottle of vexo-QR.
1 syringe.

```html
<!DOCTYPE html>
<html lang="en">
<head>
<meta charset="utf-8">
<title>Vexo QR – Intra Uterine Infusion Wash Flyer</title>
<link href="https://fonts.googleapis.com/css2?family=Montserrat:ital,wght@0,500;0,700;0,800;1,400&family=Barlow+Semi+Condensed:wght@700&family=Roboto+Condensed:wght@400;500&family=Nunito:wght@900&display=swap" rel="stylesheet">
<style>
  :root {
    --backdrop: #202020;
    --paper: #ffffff;
    --green: #00924a;
    --green-deep: #009a4e;
    --green-soft: #6abf69;
    --leaf: #5cb85c;
    --ink: #2a2d3a;
    --text: #4a4a4a;
    --tick: #e53935;
    --badge: #2b2d3a;
  }
  * { margin: 0; padding: 0; box-sizing: border-box; }
  html, body { width: 1043px; height: 1200px; overflow: hidden; background: var(--backdrop); }
  .stage { position: relative; width: 1043px; height: 1200px; }
  .flyer {
    position: absolute; left: 141px; top: 62px;
    width: 1194px; height: 1689px;
    transform: scale(0.6365); transform-origin: 0 0;
    background: var(--paper); overflow: hidden;
  }
  .photos { position: absolute; inset: 0; }
  .subtitle {
    position: absolute; left: 80px; top: 26px;
    font: italic 400 32px/33px "Montserrat", sans-serif; color: var(--text);
  }
  .headline {
    position: absolute; left: 78px; top: 108px;
    font: 700 54px/48px "Barlow Semi Condensed", sans-serif; color: var(--green);
    text-transform: uppercase;
  }
  .badge {
    position: absolute; left: 72px; top: 275px; width: 353px; height: 143px;
    background: var(--badge); border-radius: 14px;
  }
  .badge-icon { position: absolute; left: 20px; top: 20px; width: 104px; height: 104px; border-radius: 50%; background: var(--leaf); }
  .badge-rule { position: absolute; left: 141px; top: 20px; width: 2px; height: 104px; background: #fff; }
  .badge-text { position: absolute; left: 159px; top: 18px; font: 900 34px/35px "Nunito", sans-serif; color: var(--leaf); }
  .badge-text .pct { color: #fff; display: block; }
  .product-shot {
    position: absolute; left: 55px; top: 432px; width: 470px; height: 428px;
    background: linear-gradient(160deg, #f4f4f4, #dcdcdc 60%, #f2f2f2);
  }
  .benefits { position: absolute; left: 78px; top: 893px; list-style: none; width: 580px; }
  .benefits li {
    position: relative; padding-left: 37px; margin-bottom: 12px;
    font: 400 24px/30px "Roboto Condensed", sans-serif; color: var(--text);
  }
  .benefits svg { position: absolute; left: 0; top: 8px; width: 22px; height: 18px; }
  .pack {
    position: absolute; left: 86px; top: 1264px; width: 485px; height: 386px;
    border-radius: 18px; overflow: hidden; background: var(--green-soft); text-align: center; color: #fff;
  }
  .pack-title {
    background: var(--green-deep); height: 136px; padding-top: 22px;
    font: 800 48px/47px "Montserrat", sans-serif; letter-spacing: 1px;
  }
  .pack-items { padding-top: 14px; font: 500 36px/43.5px "Roboto Condensed", sans-serif; }
  .brand {
    position: absolute; left: 700px; top: 862px; width: 500px; text-align: center;
    font: 500 52px/1 "Montserrat", sans-serif; color: var(--ink); letter-spacing: 1px;
  }
  .site {
    position: absolute; left: 690px; top: 965px; width: 500px; text-align: center;
    font: 800 27px/1 "Montserrat", sans-serif; color: var(--ink);
  }
</style>
</head>
<body>
<div class="stage">
  <div class="flyer">
    <svg class="photos" width="1194" height="1689" viewBox="0 0 1194 1689">
      <defs>
        <linearGradient id="pastureTop" x1="0" y1="0" x2="0" y2="1">
          <stop offset="0" stop-color="#e9e4e2"/>
          <stop offset="0.3" stop-color="#b07a55"/>
          <stop offset="0.6" stop-color="#8a9a55"/>
          <stop offset="1" stop-color="#6f9a3c"/>
        </linearGradient>
        <linearGradient id="pastureBottom" x1="0" y1="0" x2="0" y2="1">
          <stop offset="0" stop-color="#2f9a5a"/>
          <stop offset="0.35" stop-color="#a4603a"/>
          <stop offset="0.7" stop-color="#5fae3a"/>
          <stop offset="1" stop-color="#4f9e2f"/>
        </linearGradient>
      </defs>
      <path role="img" aria-label="Photo of a Hereford cow and calf standing in a green pasture"
            fill="url(#pastureTop)" d="M500,0 H1194 V760 H660 C600,560 510,330 500,0 Z"/>
      <path role="img" aria-label="Photo of a chestnut mare and foal grazing on a green lawn"
            fill="url(#pastureBottom)" d="M700,1080 H1194 V1689 H625 C680,1500 700,1300 700,1080 Z"/>
      <circle cx="961" cy="856" r="316" fill="#ffffff"/>
    </svg>

    <p class="subtitle">An intra uterine<br>infusion wash</p>
    <h1 class="headline">Antibiotic free<br>for catlle<br>&amp; horses</h1>

    <div class="badge">
      <span class="badge-icon"></span>
      <span class="badge-rule"></span>
      <p class="badge-text"><span class="pct">100%</span>PLANT<br>EXTRACTS</p>
    </div>

    <div class="product-shot" role="img" aria-label="Product photo: vexo-QR bottle, box, pipette and syringe"></div>

    <ul class="benefits">
      <li><svg viewBox="0 0 22 18"><path d="M2,9 L8,15 L20,2" fill="none" stroke="var(--tick)" stroke-width="3"/></svg>Base product starts with human homeopathy formula and with the same team of doctors, created vexo-QR.</li>
      <li><svg viewBox="0 0 22 18"><path d="M2,9 L8,15 L20,2" fill="none" stroke="var(--tick)" stroke-width="3"/></svg>Produced in a laboratory that is certified human grade.</li>
      <li><svg viewBox="0 0 22 18"><path d="M2,9 L8,15 L20,2" fill="none" stroke="var(--tick)" stroke-width="3"/></svg>Standard meets &amp; exceeds all EU and USA requirements</li>
      <li><svg viewBox="0 0 22 18"><path d="M2,9 L8,15 L20,2" fill="none" stroke="var(--tick)" stroke-width="3"/></svg>Trials include a university in Germany.</li>
      <li><svg viewBox="0 0 22 18"><path d="M2,9 L8,15 L20,2" fill="none" stroke="var(--tick)" stroke-width="3"/></svg>On farms trials, in Asia, Europe, USA, Australia &amp; Canada.</li>
      <li><svg viewBox="0 0 22 18"><path d="M2,9 L8,15 L20,2" fill="none" stroke="var(--tick)" stroke-width="3"/></svg>No milk and meat withdrawals.</li>
      <li><svg viewBox="0 0 22 18"><path d="M2,9 L8,15 L20,2" fill="none" stroke="var(--tick)" stroke-width="3"/></svg>Produced in The Netherlands &amp; we meet U.S.<br>and European standards.</li>
    </ul>

    <div class="pack">
      <div class="pack-title">10 DOSES<br>READY TO USE</div>
      <div class="pack-items">25 mL. Per dose<br>10 Pipettes<br>1 bottle of 250 mL<br>vexo-QR.<br>1 35 ML syringe.</div>
    </div>

    <p class="brand">VEXO QR</p>
    <p class="site">www.vexo-qr.examplestore.test</p>
  </div>
</div>
</body>
</html>
```